VELOXA SPORTS NETWORK

design a website that will be a companion to a sports network that features womens sports and fitness content.
With the goal of promoting and empowering female athleticism, Veloxatv.example will be the online network that connects female sports fans to the sports they love and follow. The site aims to raise the level of awareness of women in sports by providing comprehensive sports coverage, spotlighting outstanding achievements, and working with sporting associations on advocacy issues and empowering programs.
Updates
I would like to have all entry by Sunday June 8 2014 thank you
please use actual script not lorem ipsum
thank you
Deadline winding down, added new pictures to file
Target Market(s)
our target market is females 18-54, whom love womens sports and ftiness
Industry/Entity Type
Fitness
Requirements
Must have
- Attributes of the website:
1. Large Photos: to accompany current stories
2. Colorful: Highlight Veloxa’s officials colors
3. News Area: recent news items on the home page and achieved news stories
4. Featured Content area: Headline news, athlete spotlights and issues
5. Streaming content: to accompany news and featured content
6. Advertiser links: to purchase merchandise
7. Real-time scores of live events
8. Blog
9. Monthly newsletter
10. Athlete profile page
11. Model close to QRVT
Nice to have
- Veloxatv.example will offer value-added service that will entitle customers to gain access to online streaming services provided by Veloxa, which delivers both live streams and on-demand replays of global women’s sports events to sports fans in U.S. and abroad. This service will be subscription based for a modest monthly fee. Content will be available across multiple platforms and cloud based. New subscriber will get first 30 days free.
Content will include:
1. Live sports events
2. On-demand and premium content
3. Fan-generated Content

```html
<!DOCTYPE html>
<html lang="en">
<head>
<meta charset="utf-8">
<title>Veloxa Sports Network</title>
<link rel="stylesheet" href="https://fonts.googleapis.com/css2?family=Oswald:wght@400;500&family=Open+Sans:ital,wght@0,400;0,600;0,700;1,400&family=PT+Sans+Narrow:wght@400;700&display=swap">
<style>
  :root {
    --red: #e8262b;
    --red-deep: #d91f26;
    --red-warm: #f0452e;
    --ink: #2b2b2b;
    --grey: #5a5a5a;
    --pale: #f4f4f4;
    --white: #ffffff;
  }
  * { box-sizing: border-box; margin: 0; padding: 0; }
  html, body { width: 788px; height: 1200px; overflow: hidden; background: var(--white); }
  body { position: relative; font-family: "Open Sans", sans-serif; color: var(--ink); }
  .abs { position: absolute; }

  /* header */
  .topbar { left: 0; top: 0; width: 788px; height: 48px; background: var(--white); }
  .scorebar { left: 0; top: 48px; width: 788px; height: 36px; background: var(--pale); }
  .score-link { top: 57px; font: 700 12px "PT Sans Narrow", sans-serif; color: var(--red); }
  .nav-link { top: 16px; font: 700 12.5px "PT Sans Narrow", sans-serif; color: var(--grey); letter-spacing: .3px; }
  .nav-link.account { color: var(--red); }
  .brand { left: 32px; top: 4px; width: 138px; height: 94px; background: var(--white);
           box-shadow: 0 1px 4px rgba(0,0,0,.25); display: flex; flex-direction: column;
           align-items: center; justify-content: center; gap: 6px; z-index: 2; }
  .brand-dot { width: 26px; height: 26px; border-radius: 50%; background: var(--red); }
  .brand-name { font: 700 14px "Open Sans", sans-serif; color: var(--red); letter-spacing: 1px; }

  /* hero */
  .hero-photo { left: 0; top: 84px; width: 600px; height: 158px;
                background:
                  radial-gradient(ellipse 140px 120px at 170px 80px, rgba(60,50,50,.55), transparent 70%),
                  radial-gradient(ellipse 90px 60px at 90px 60px, rgba(201,143,131,.7), transparent 70%),
                  linear-gradient(90deg, #c9bdb7 0%, #dedad8 40%, #ececec 100%); }
  .hero-copy { right: 210px; top: 104px; text-align: right; color: var(--red); }
  .hero-title { font: 700 25px "Open Sans", sans-serif; line-height: 1.1; }
  .hero-sub { font: italic 400 24px "Open Sans", sans-serif; line-height: 1.2; }
  .hero-service { font: 700 19px "Open Sans", sans-serif; line-height: 1.3; margin-top: 4px; }

  /* sidebar */
  .sidebar { left: 602px; top: 84px; width: 186px; height: 432px;
             background: linear-gradient(180deg, var(--red-deep), var(--red-warm)); }
  .side-label { font: 700 13px "PT Sans Narrow", sans-serif; color: var(--white); }
  .stream-thumb { left: 623px; width: 137px; height: 68px; }
  .stream-photo { width: 100%; height: 100%;
                  background: linear-gradient(180deg, #8fa8b8 0%, #b07a6c 55%, #c85a48 100%); }
  .stream-cap { position: absolute; left: 0; bottom: 0; width: 100%; height: 16px; background: rgba(40,40,40,.85);
                color: var(--white); font: 700 10px "Open Sans", sans-serif; text-align: center; line-height: 16px; }
  .features { left: 612px; top: 298px; width: 163px; height: 184px; background: var(--red-warm); }
  .feature-item { font: 700 12.5px "PT Sans Narrow", sans-serif; color: var(--white); line-height: 1.05; }
  .trial-btn { left: 637px; top: 444px; width: 138px; height: 36px; background: var(--white);
               box-shadow: 0 3px 0 #444; font: 700 13px "Open Sans", sans-serif; color: var(--ink);
               display: flex; align-items: center; justify-content: center; }

  /* news */
  .news-heading { left: 22px; top: 262px; font: 400 38px "Oswald", sans-serif; color: var(--ink); }
  .news-photo { left: 122px; width: 115px; height: 86px;
                background: linear-gradient(180deg, #5c6a3e 0%, #9b6b52 45%, #c8503f 70%, #e6dcd2 100%); }
  .news-title { left: 247px; font: 700 19px "Open Sans", sans-serif; color: var(--ink); white-space: nowrap; }
  .news-text { left: 247px; width: 330px; font: 400 11.5px "PT Sans Narrow", sans-serif; color: var(--ink); line-height: 1.4; }

  /* blog and merchandise */
  .blog-band { left: 0; top: 580px; width: 459px; height: 200px;
               background: linear-gradient(135deg, var(--red-deep), var(--red-warm)); }
  .merch-box { left: 461px; top: 580px; width: 327px; height: 200px; background: var(--white);
               border: 2px solid var(--red); }
  .section-title { font: 400 25px "Oswald", sans-serif; }
  .blog-photo { top: 644px; height: 74px; background: linear-gradient(180deg, #e9eef2 0%, #c2a596 50%, #8c9a74 100%); }
  .blog-cap { top: 726px; font: 700 10.5px "Open Sans", sans-serif; color: var(--white); text-align: right; line-height: 1.4; white-space: nowrap; }
  .merch-item { top: 638px; height: 70px; }
  .merch-price { top: 720px; width: 48px; text-align: center; font: 700 12px "PT Sans Narrow", sans-serif; color: var(--red); line-height: 1.1; }

  /* testimonials */
  .testimonial-band { left: 0; top: 780px; width: 788px; height: 235px;
                      background:
                        radial-gradient(ellipse 160px 90px at 110px 60px, rgba(214,200,90,.45), transparent 70%),
                        linear-gradient(90deg, #c58676, #e5a899 50%, #cf8e80); }
  .testimonial-title { left: 0; top: 832px; width: 788px; text-align: center; font: 400 44px "Oswald", sans-serif; color: #111; }
  .testimonial-text { left: 94px; top: 901px; width: 600px; text-align: center; font: 400 15px "PT Sans Narrow", sans-serif; color: #111; line-height: 1.3; }

  /* footer */
  .footer { left: 0; top: 1015px; width: 788px; height: 185px;
            background: linear-gradient(180deg, var(--red-deep), var(--red-warm)); }
  .foot-head { top: 1054px; font: 700 14px "PT Sans Narrow", sans-serif; color: var(--white); }
  .foot-links { top: 1078px; font: 400 11px "PT Sans Narrow", sans-serif; color: var(--white); text-align: right; line-height: 20px; }
  .newsletter-title { left: 499px; top: 1050px; font: 400 21px "Oswald", sans-serif; color: var(--white); }
  .newsletter-input { left: 499px; top: 1080px; width: 142px; height: 26px; background: var(--white);
                      font: 700 13px "PT Sans Narrow", sans-serif; color: var(--red); padding: 4px 6px; }
  .newsletter-btn { left: 641px; top: 1080px; width: 76px; height: 26px; background: #2a2a2a; color: var(--white);
                    font: 400 13px "Open Sans", sans-serif; text-align: center; line-height: 26px; }
  .social { left: 610px; top: 1126px; display: flex; gap: 5px; }
  .social span { width: 18px; height: 18px; border-radius: 50%; background: var(--white); display: block; }
  .copyright { left: 0; top: 1180px; width: 788px; text-align: center; font: 400 11px "PT Sans Narrow", sans-serif; color: var(--white); }
</style>
</head>
<body>

<header>
  <div class="abs topbar"></div>
  <div class="abs scorebar"></div>
  <div class="abs brand"><span class="brand-dot"></span><span class="brand-name">VELOXA</span></div>
  <nav>
    <span class="abs nav-link" style="left:281px">ABOUT</span>
    <span class="abs nav-link" style="left:404px">BLOG</span>
    <span class="abs nav-link" style="left:519px">MERCHANDISE</span>
    <span class="abs nav-link account" style="left:662px">REGISTER | LOG IN</span>
  </nav>
  <span class="abs score-link" style="left:342px">Real-time scores of live events</span>
  <span class="abs score-link" style="left:606px">Real-time scores of live events</span>
</header>

<section>
  <div class="abs hero-photo" role="img" aria-label="Athlete stretching in a gym"></div>
  <div class="abs hero-copy">
    <div class="hero-title">WELCOME TO VELOXA</div>
    <div class="hero-sub">women's sports, all access</div>
    <div class="hero-service">ONLINE STREAMING<br>SERVICES</div>
  </div>
</section>

<aside>
  <div class="abs sidebar"></div>
  <span class="abs side-label" style="left:621px;top:94px">STREAMING LIVE</span>
  <div class="abs stream-thumb" style="top:117px">
    <div class="stream-photo" role="img" aria-label="Hurdlers racing on a track"></div>
    <div class="stream-cap">HURDLES FINAL LIVE</div>
  </div>
  <div class="abs stream-thumb" style="top:191px">
    <div class="stream-photo" role="img" aria-label="Runners in a stadium race"></div>
    <div class="stream-cap">10,000M RACE LIVE</div>
  </div>
  <span class="abs side-label" style="left:625px;top:262px;font-weight:400">See All</span>
  <div class="abs features"></div>
  <span class="abs side-label" style="left:628px;top:312px;font-size:15px">FEATURES</span>
  <span class="abs feature-item" style="left:627px;top:340px">LIVE SPORTS EVENTS</span>
  <span class="abs feature-item" style="left:624px;top:364px">ON-DEMAND AND PREMIUM<br>CONTENT</span>
  <span class="abs feature-item" style="left:624px;top:403px">FAN-GENERATED CONTENT</span>
  <div class="abs trial-btn">Free 30 days trial</div>
</aside>

<section>
  <h2 class="abs news-heading">NEWS</h2>
  <div class="abs news-photo" style="top:266px" role="img" aria-label="Runners celebrating at the finish line"></div>
  <h3 class="abs news-title" style="top:270px">RELAY TEAM TAKES GOLD</h3>
  <p class="abs news-text" style="top:301px">A LATE SURGE ON THE FINAL LEG SEALS A RECORD WIN AND A FIRST TITLE IN TWELVE YEARS</p>
  <div class="abs news-photo" style="top:373px" role="img" aria-label="Distance runners in a race"></div>
  <h3 class="abs news-title" style="top:377px">MARATHON COMEBACK</h3>
  <p class="abs news-text" style="top:408px">BACK FROM INJURY, SHE RUNS A PERSONAL BEST AND EARNS A PLACE ON THE NATIONAL TEAM</p>
  <div class="abs news-photo" style="top:479px" role="img" aria-label="Sprinter crossing the finish line"></div>
  <h3 class="abs news-title" style="top:483px">SPRINT STAR ON FIRE</h3>
  <p class="abs news-text" style="top:514px">THREE RACES, THREE WINS: THE 200M CHAMPION KEEPS HER UNBEATEN SEASON ALIVE</p>
</section>

<section>
  <div class="abs blog-band"></div>
  <h2 class="abs section-title" style="left:27px;top:588px;color:var(--white)">BLOG</h2>
  <div class="abs blog-photo" style="left:34px;width:108px" role="img" aria-label="Marathon runners on a road"></div>
  <div class="abs blog-photo" style="left:175px;width:117px" role="img" aria-label="Women jogging in a park"></div>
  <div class="abs blog-photo" style="left:328px;width:111px;background:linear-gradient(180deg,#bfe3f2 0%,#f2c46b 60%,#9cc45a 100%)" role="img" aria-label="Fruit smoothies in glasses"></div>
  <div class="abs blog-cap" style="left:34px;width:114px">RACE DAY PREP TIPS<br><span style="font-weight:400;font-size:11px">Jun 1, 2014</span></div>
  <div class="abs blog-cap" style="left:180px;width:114px">RUNNING TOGETHER<br><span style="font-weight:400;font-size:11px">Jun 1, 2014</span></div>
  <div class="abs blog-cap" style="left:328px;width:114px">POST-RUN SMOOTHIES<br><span style="font-weight:400;font-size:11px">Jun 1, 2014</span></div>

  <div class="abs merch-box"></div>
  <h2 class="abs section-title" style="left:496px;top:590px;color:var(--red)">MERCHANDISE</h2>
  <div class="abs merch-item" style="left:493px;width:59px;background:linear-gradient(180deg,#e53b72,#5b7fc8)" role="img" aria-label="Pink running shorts"></div>
  <div class="abs merch-item" style="left:574px;width:59px;background:#d42c7c" role="img" aria-label="Pink long-sleeve top"></div>
  <div class="abs merch-item" style="left:658px;width:38px;background:#1c1c1c" role="img" aria-label="Black running tights"></div>
  <div class="abs merch-item" style="left:722px;width:48px;background:#2a2a2a" role="img" aria-label="Black long-sleeve top"></div>
  <span class="abs merch-price" style="left:496px">Shorts<br>$79</span>
  <span class="abs merch-price" style="left:569px">Top<br>$79</span>
  <span class="abs merch-price" style="left:647px">Tights<br>$79</span>
  <span class="abs merch-price" style="left:729px">Jersey<br>$79</span>
</section>

<section>
  <div class="abs testimonial-band" role="img" aria-label="Woman doing a floor workout"></div>
  <h2 class="abs testimonial-title">Testimonials</h2>
  <p class="abs testimonial-text">“Finally a network that treats women's sport like it matters. I watch every final live and catch up on the replays on my phone during my commute. It keeps me training and cheering all season.”</p>
</section>

<footer>
  <div class="abs footer"></div>
  <span class="abs foot-head" style="left:73px">Navigation</span>
  <span class="abs foot-head" style="left:195px">Product Info</span>
  <span class="abs foot-head" style="left:333px">Useful Info</span>
  <div class="abs foot-links" style="left:60px;width:68px">Home<br>About Us<br>Our Products<br>Contact Us</div>
  <div class="abs foot-links" style="left:200px;width:60px">Live Events<br>On-Demand<br>Premium<br>Fan Content</div>
  <div class="abs foot-links" style="left:300px;width:90px">Privacy Policy<br>Terms &amp; Agreement<br>FAQ<br>SiteMap</div>
  <span class="abs newsletter-title">Monthly Newsletter</span>
  <div class="abs newsletter-input">Enter e-mail</div>
  <div class="abs newsletter-btn">Subscribe</div>
  <div class="abs social" aria-label="Social links"><span></span><span></span><span></span><span></span><span></span></div>
  <div class="abs copyright">CopyRight 2014 Veloxatv.example</div>
</footer>

</body>
</html>
```